E-commerce- Online Web Design Project

Needed: Web Design for an e-commerce website based in Kuwait called : Dovrani - which is the equivalent to " Everything" This website will be selling everything from - Electronics & Computers, health & beauty products, video games, Home Goods, Pet Supplies, Baby & Toddler, etc. Sale section.( Front End)
Then you have the Back End ( where the vendors go to upload their products)
Along with the different pages that comes with the project of an online store- about us- contact page- live chat ( operator) etc.
Industry/Entity Type
E-Commerce
Look and feel
Each slider illustrates characteristics of the customer's brand and the style your logo design should communicate.

```html
<!DOCTYPE html>
<html lang="en">
<head>
<meta charset="utf-8">
<title>Dovrani – Shop anything in one website</title>
<link rel="stylesheet" href="https://fonts.googleapis.com/css2?family=Arimo:wght@400;700&family=PT+Sans+Narrow:wght@400;700&display=swap">
<style>
  :root {
    --header-bg: #1d0303;
    --page-bg: #5b2b12;
    --page-bg-dark: #3e1a08;
    --panel: #ffffff;
    --ink: #2a0a05;
    --ink-soft: #3a2a25;
    --brown: #6a2c12;
    --rule: #d9c9c0;
    --card: #f3ece6;
    --price: #a8121a;
    --muted: #d8d0cc;
    --banner-light: #fdf2c9;
    --banner-warm: #f6d27e;
    --banner-border: #d3a46a;
  }
  * { box-sizing: border-box; margin: 0; padding: 0; }
  html, body { width: 1200px; height: 800px; overflow: hidden; }
  body {
    position: relative;
    font-family: "Arimo", Arial, sans-serif;
    color: var(--ink);
    background: linear-gradient(90deg, var(--page-bg-dark) 0%, var(--page-bg) 8%, var(--page-bg) 92%, var(--page-bg-dark) 100%);
  }
  .site-header {
    position: absolute; left: 0; top: 0; width: 1200px; height: 165px;
    background: var(--header-bg);
    box-shadow: 0 3px 6px rgba(0,0,0,.5);
    z-index: 2;
  }
  .page-panel {
    position: absolute; left: 98px; top: 160px; width: 1002px; height: 640px;
    background: var(--panel);
    box-shadow: 0 0 12px rgba(0,0,0,.45);
  }
  .brand {
    position: absolute; left: 113px; top: 0; width: 183px; height: 220px;
    background: var(--panel);
    border: 1px solid #c9bdb6;
    box-shadow: 0 2px 4px rgba(0,0,0,.25);
    z-index: 3;
    display: flex; flex-direction: column; align-items: center; justify-content: center; gap: 14px;
  }
  .brand-square { width: 26px; height: 26px; background: var(--brown); }
  .brand-name { font-family: "PT Sans Narrow", sans-serif; font-size: 40px; font-weight: 400; color: var(--ink); }

  .contact { position: absolute; right: 130px; top: 22px; text-align: right; color: #fff; z-index: 3; }
  .contact-label { font-size: 15px; }
  .contact-phone { font-size: 21px; color: var(--muted); margin-top: 6px; }
  .search {
    position: absolute; left: 868px; top: 82px; width: 202px; height: 28px; z-index: 3;
    background: linear-gradient(#fff, #ede4dd); border: 1px solid #b99c8c; border-radius: 5px;
    font-size: 12px; color: #8a6c5c; padding: 7px 0 0 11px;
  }
  .search svg { position: absolute; right: 5px; top: 3px; }
  .account-nav { position: absolute; right: 128px; top: 128px; z-index: 3; font-size: 12.5px; color: #fff; display: flex; gap: 6px; }
  .account-nav span.dot { color: #bbb; }

  .sidebar { position: absolute; left: 128px; top: 234px; width: 159px; z-index: 3; }
  .side-heading { font-family: "PT Sans Narrow", sans-serif; font-size: 20px; color: var(--ink); height: 36px; border-bottom: 1px solid var(--rule); }
  .side-list { list-style: none; font-size: 11px; color: var(--ink); }
  .side-list > li { height: 30px; line-height: 30px; padding-left: 12px; border-bottom: 1px solid var(--rule); }
  .side-list > li.active { font-weight: 700; height: auto; }
  .active-label::before { content: "▸"; font-size: 9px; margin-right: 5px; }
  .sub-list { list-style: none; font-weight: 400; padding: 0 0 4px 10px; }
  .sub-list li { height: 22px; line-height: 22px; }
  .sub-list li::before { content: "➜"; font-size: 7px; margin-right: 6px; }
  .refine { margin-top: 27px; }
  .check-list { list-style: none; position: relative; font-size: 11px; padding: 4px 0 2px 24px; border-bottom: 1px solid var(--rule); }
  .check-list li { height: 22px; line-height: 22px; }
  .check-list li::before { content: ""; display: inline-block; width: 9px; height: 9px; border: 1px solid var(--ink); margin-right: 9px; vertical-align: -1px; }
  .scroll-track { position: absolute; right: 8px; top: 8px; width: 2px; height: 54px; background: #bbb; }
  .scroll-track::before, .scroll-track::after { content: ""; position: absolute; left: -3px; border: 4px solid transparent; }
  .scroll-track::before { top: -7px; border-bottom-color: var(--ink); border-top: 0; }
  .scroll-track::after { bottom: -7px; border-top-color: var(--ink); border-bottom: 0; }

  .hero {
    position: absolute; left: 311px; top: 179px; width: 763px; height: 253px; z-index: 3;
    border: 1px solid var(--banner-border);
    background: linear-gradient(90deg, var(--banner-light) 0%, #fcecb6 55%, var(--banner-warm) 100%);
    overflow: hidden;
  }
  .hero-title { position: absolute; left: 40px; top: 46px; font-family: "PT Sans Narrow", sans-serif; font-weight: 700; font-size: 47px; line-height: 51px; color: var(--ink); }
  .hero-title em { font-style: normal; color: var(--brown); }
  .hero-button {
    position: absolute; left: 101px; top: 166px; width: 144px; height: 41px; border-radius: 7px;
    background: linear-gradient(#7e3519, #5a210c); border: 2px solid #e7b07a;
    color: #fff; font-family: "PT Sans Narrow", sans-serif; font-size: 18px; text-align: center; line-height: 37px;
  }
  .hero-photo { position: absolute; right: 0; top: 0; width: 310px; height: 251px; background: linear-gradient(160deg, #f7cf86, #e58b3a 55%, #2e4d8f 100%); opacity: .55; }

  .featured { position: absolute; left: 311px; top: 452px; width: 762px; z-index: 3; }
  .featured-heading { font-family: "PT Sans Narrow", sans-serif; font-weight: 700; font-size: 17px; color: var(--ink); padding-bottom: 5px; width: 230px; border-bottom: 1px solid; border-image: linear-gradient(90deg, #999, transparent) 1; }
  .view-bar { display: flex; justify-content: space-between; font-size: 11px; margin-top: 13px; color: var(--ink); }
  .products { display: flex; gap: 5px; margin-top: 11px; }
  .product { width: 186px; height: 300px; background: var(--card); padding: 6px; }
  .product-photo { height: 182px; background: #fff; border: 1px solid var(--rule); display: flex; align-items: center; justify-content: center; }
  .product-photo span { width: 110px; height: 120px; border-radius: 10px; }
  .product-name { font-size: 12px; font-weight: 700; line-height: 17px; margin-top: 9px; padding-left: 2px; }
  .product-code { font-size: 12px; margin-top: 7px; padding-left: 2px; color: var(--ink-soft); }
  .product-price { font-size: 16px; font-weight: 700; color: var(--price); margin-top: 8px; padding-left: 2px; }
</style>
</head>
<body>
  <header class="site-header"></header>
  <div class="page-panel"></div>

  <div class="brand">
    <span class="brand-square"></span>
    <span class="brand-name">Dovrani</span>
  </div>

  <div class="contact">
    <div class="contact-label">Contact us now</div>
    <div class="contact-phone">012.555.0148</div>
  </div>
  <div class="search">Search Here
    <svg width="24" height="22" viewBox="0 0 24 22"><circle cx="10" cy="9" r="7" fill="none" stroke="#4a2a1a" stroke-width="2"/><line x1="15" y1="14" x2="21" y2="20" stroke="#4a2a1a" stroke-width="3" stroke-linecap="round"/></svg>
  </div>
  <nav class="account-nav">
    <span>My Account</span><span class="dot">•</span><span>My Wishlist</span><span class="dot">•</span><span>My Cart</span><span class="dot">•</span><span>Checkout</span><span class="dot">•</span><span>Log In</span>
  </nav>

  <aside class="sidebar">
    <h2 class="side-heading">CATEGORIES</h2>
    <ul class="side-list">
      <li>JACKETS</li>
      <li class="active"><span class="active-label">TOPS</span>
        <ul class="sub-list"><li>SLEEVLESS</li><li>SHORT SLEEVS</li><li>LONG SLEEVS</li></ul>
      </li>
      <li>COMPUTER</li>
      <li>DRESSES</li>
      <li>ELECTRONICS</li>
      <li>HEALTH</li>
      <li>VIDEO GAMES</li>
      <li>ALL COLLECTIONS</li>
    </ul>
    <h2 class="side-heading refine">REFINE BY</h2>
    <ul class="side-list">
      <li class="active"><span class="active-label">PRODUCT TYPE</span></li>
    </ul>
    <ul class="check-list">
      <li>LOREM</li><li>IPSUM</li><li>DOLOR</li>
      <span class="scroll-track"></span>
    </ul>
    <ul class="side-list">
      <li>TYPE</li>
      <li>COLOR</li>
    </ul>
  </aside>

  <section class="hero">
    <h1 class="hero-title">Shop anything in<br><em>one website</em></h1>
    <div class="hero-button">LEARN MORE</div>
    <div class="hero-photo" role="img" aria-label="Photo of a smiling shopper in a blue jacket holding colourful shopping bags"></div>
  </section>

  <section class="featured">
    <h2 class="featured-heading">FEATURED PRODUCT</h2>
    <div class="view-bar"><span>LIST VIEW &nbsp;| &nbsp;GRID VIEW</span><span>PAGE 1 OF 15 &nbsp;| &nbsp;VIEW ALL</span></div>
    <div class="products">
      <article class="product">
        <div class="product-photo"><span role="img" aria-label="Photo of a silver laptop" style="background:linear-gradient(#3a5d9c,#c9ccd2)"></span></div>
        <div class="product-name">PRODUCT DETAILS PRODU-<br>CT DETAILS</div>
        <div class="product-code">ITEM CODE: 0000000</div>
        <div class="product-price">$ 500.00</div>
      </article>
      <article class="product">
        <div class="product-photo"><span role="img" aria-label="Photo of a colourful stacking ring toy" style="background:linear-gradient(#e0482a,#f4c72c,#3aa83a,#2a8fd0,#e12a2a)"></span></div>
        <div class="product-name">PRODUCT DETAILS PRODU-<br>CT DETAILS</div>
        <div class="product-code">ITEM CODE: 0000000</div>
        <div class="product-price">$ 500.00</div>
      </article>
      <article class="product">
        <div class="product-photo"><span role="img" aria-label="Photo of a blue portable music player" style="background:linear-gradient(#1f5fb0,#4a8fe0)"></span></div>
        <div class="product-name">PRODUCT DETAILS PRODU-<br>CT DETAILS</div>
        <div class="product-code">ITEM CODE: 0000000</div>
        <div class="product-price">$ 500.00</div>
      </article>
      <article class="product">
        <div class="product-photo"><span role="img" aria-label="Photo of a red dress on a hanger" style="background:linear-gradient(#f0323a,#c8101c)"></span></div>
        <div class="product-name">PRODUCT DETAILS PRODU-<br>CT DETAILS</div>
        <div class="product-code">ITEM CODE: 0000000</div>
        <div class="product-price">$ 500.00</div>
      </article>
    </div>
  </section>
</body>
</html>
```